BRISKWATER MOTION GYM FLYER DESIGN

We want a flyer designed for our gym. We have an example of a flyer which we like and I have put it into the images I have uploaded. I would like to recreate using our pictures, so its a pretty straight forward job. We also want to put our weekly timetable on the back of the flyer. We would like the size of the flyer to be A5.

Target Market(s)

FITNESS

Industry/Entity Type

Gym

Colors
33a6d7
ffffff

Requirements
Must have
• We just want to recreate the flyer but we must have the following info on the flyer and we want our timetable on the back of the flyer which you can get from this link: http://www.briskwatermotiongym.com/timetable
• Briskwater Motion Gym is a fun community of humble people. Our goal is to help guide you towards a fitter, healthier lifestyle!
• Our Programs
• HIIT
• High intensity interval training is 30-45 minutes of fat burning fun. The class is a mix of cardio, bodyweight and some resistance movements.
• Conditioning
• A full hour of strength, cardio and bodyweight training to get you in tip top shape. Expect a mix of barbells, kettlebells, rowing machines, bikes and other training methods.
• KPL
• This is our big Friday session to set you up for the weekend. 90 minutes of hard training that is done with a team emphasis. From heavy lifting to cardio triathlons, this class has it all but not for the faint hearted.
• Muay Thai
• Commonly known as the science of 8 limbs you will learn how to punch, kick, knee and elbow. Thailands national sport is a great way to get your fitness kick. We train the complete beginner all the way to international fighters so you are in great hands.
• Kids Muay Thai
• Our junior program starts from age 6 onwards. Muay Thai is a great way for kids to get active and fit while learning new skills. Training in martial arts also teaches self discipline and socialisation skills.
• Yoga
• A combination of physical and mental practises that will leave you focused and refreshed for whatever the week throws at you. We always recommend our yoga classes as a great way to balance the high intensity training we offer.
• U-Press
• Strength training with a little bit of conditioning. We regularly update the program and re test lifts to ensure you are making progress and getting stronger.
• CONTACT US
• OUR LOCATION:
• Unit 42C
• 273 Quillan Street
• Fenwick Hollow
• Glasgow
• G72TR
• Phone: 07950362814
• Email: info@briskwatermotiongym.com
• Web: www.briskwatermotiongym.com
Nice to have
• Can use all the picture but if not be good to use the boxing one and the group training one.

```html
<!DOCTYPE html>
<html lang="en">
<head>
<meta charset="utf-8">
<title>Briskwater Motion Gym – Flyer</title>
<link href="https://fonts.googleapis.com/css2?family=Orbitron:wght@500;700;900&family=Roboto+Condensed:wght@400;700&family=Roboto:wght@300;400;500&display=swap" rel="stylesheet">
<style>
  :root {
    --brand-blue: #1fa9e6;
    --brand-navy: #0d1d63;
    --navy-light: #14308f;
    --ink: #111216;
    --copy: #16224f;
    --white: #ffffff;
    --page: #eef0f2;
  }
  * { box-sizing: border-box; margin: 0; padding: 0; }
  html, body { width: 1200px; height: 846px; overflow: hidden; background: var(--page); }
  .flyer {
    position: absolute; left: 50px; top: 34px; width: 1100px; height: 778px;
    background: var(--brand-blue); overflow: hidden;
    box-shadow: 0 4px 14px rgba(0,0,0,.18);
  }

  /* Left column */
  .intro { position: absolute; left: 0; top: 0; width: 350px; height: 455px; background: var(--brand-blue); }
  .headline { position: absolute; left: 0; top: 38px; width: 350px; text-align: center; font-family: "Orbitron", sans-serif; }
  .headline .lead { display: block; font-size: 29px; font-weight: 700; color: var(--ink); letter-spacing: .5px; }
  .headline .punch { display: block; font-size: 40px; font-weight: 900; color: var(--white); margin-top: 2px; letter-spacing: 1px; }
  .intro-shapes { position: absolute; left: 0; top: 0; }
  .intro-copy { position: absolute; left: 25px; top: 178px; width: 300px; text-align: center; font-family: "Roboto", sans-serif; color: var(--brand-blue); }
  .intro-copy p { font-size: 16.5px; line-height: 22px; }
  .intro-copy p.goal { font-weight: 500; font-size: 17.5px; line-height: 24px; margin-top: 12px; }
  .join { position: absolute; left: 0; top: 398px; width: 350px; text-align: center; }
  .join-title { font-family: "Roboto", sans-serif; font-weight: 500; font-size: 22px; color: var(--ink); display: flex; align-items: center; justify-content: center; gap: 12px; }
  .join-title::before, .join-title::after { content: ""; width: 42px; height: 4px; background: var(--white); }
  .join-web { font-family: "Orbitron", sans-serif; font-weight: 500; font-size: 13.5px; color: var(--white); margin-top: 6px; }
  .photo-boxing { position: absolute; left: 0; top: 455px; width: 350px; height: 323px;
    background: linear-gradient(160deg, #5b6570 0%, #2e3238 45%, #1b1d21 100%); }

  /* Right column */
  .programs { position: absolute; left: 350px; top: 0; width: 750px; height: 778px; }
  .photo-group { position: absolute; left: 0; top: 0; width: 750px; height: 390px;
    background: linear-gradient(180deg, #3a3d41 0%, #26292c 55%, #2f4a33 80%, #1f2a22 100%); }
  .programs-shapes { position: absolute; left: 0; top: 0; }
  .section-title { position: absolute; left: 340px; top: 262px; font-family: "Orbitron", sans-serif; font-weight: 900;
    font-size: 33px; letter-spacing: 5px; color: var(--brand-blue); transform: rotate(-7deg); transform-origin: left bottom; }

  .program-col { position: absolute; font-family: "Roboto Condensed", sans-serif; color: var(--copy); font-size: 12.8px; line-height: 17.3px; }
  .program-col h2 { font-family: "Orbitron", sans-serif; font-weight: 700; font-size: 18px; color: var(--white); letter-spacing: 1px; line-height: 22px; margin-bottom: 4px; }
  .program-col p { margin-bottom: 12px; }
  .col-one { left: 46px; top: 378px; width: 218px; }
  .col-two { left: 298px; top: 358px; width: 208px; }
  .col-three { left: 520px; top: 322px; width: 200px; }

  .contact { position: absolute; right: 22px; top: 634px; text-align: right; }
  .contact h3 { font-family: "Orbitron", sans-serif; font-weight: 700; font-size: 25px; line-height: 30px; color: var(--brand-blue); letter-spacing: 1px; }
  .contact .phone { font-family: "Roboto", sans-serif; font-weight: 300; font-size: 27px; line-height: 32px; color: var(--white); margin-top: 4px; letter-spacing: 1px; }
  .contact .email { font-family: "Roboto", sans-serif; font-weight: 500; font-size: 14px; color: var(--brand-blue); margin-top: 4px; }
  .footer-web { position: absolute; left: 18px; top: 748px; font-family: "Orbitron", sans-serif; font-weight: 700; font-size: 12.5px; color: var(--brand-blue); letter-spacing: .5px; }
  .address { position: absolute; right: 30px; top: 750px; font-family: "Roboto", sans-serif; font-size: 14px; color: var(--ink); }
</style>
</head>
<body>
<main class="flyer">
  <section class="intro">
    <svg class="intro-shapes" width="350" height="455" viewBox="0 0 350 455" aria-hidden="true">
      <defs>
        <linearGradient id="navyPanel" x1="0" y1="0" x2="1" y2="1">
          <stop offset="0" stop-color="#0a1650"/>
          <stop offset="1" stop-color="#14308f"/>
        </linearGradient>
      </defs>
      <rect x="0" y="130" width="350" height="244" fill="url(#navyPanel)"/>
      <polygon points="190,130 230,130 210,152" fill="#1fa9e6"/>
      <polygon points="192,373 228,373 210,392" fill="#12287c"/>
    </svg>
    <h1 class="headline"><span class="lead">NO EXPERIENCE?</span><span class="punch">NO PROBLEM</span></h1>
    <div class="intro-copy">
      <p>Briskwater Motion Gym is a fun community of humble people.</p>
      <p class="goal">Our goal is to help guide you towards a fitter, healthier lifestyle!</p>
    </div>
    <div class="join">
      <div class="join-title">JOIN TODAY</div>
      <div class="join-web">www.BriskwaterMotionGym.com</div>
    </div>
  </section>
  <div class="photo-boxing" role="img" aria-label="Photo of a woman training with battle ropes in the boxing gym"></div>

  <section class="programs">
    <div class="photo-group" role="img" aria-label="Photo of a group kettlebell class on the gym floor"></div>
    <svg class="programs-shapes" width="750" height="778" viewBox="0 0 750 778" aria-hidden="true">
      <polygon points="0,375 750,300 750,778 0,778" fill="#1fa9e6"/>
      <polygon points="290,340 750,238 750,300 290,346" fill="#111216"/>
      <polygon points="0,740 470,724 578,624 750,610 750,778 0,778" fill="#111216"/>
      <polygon points="282,778 300,740 750,740 750,778" fill="#ffffff"/>
    </svg>
    <h2 class="section-title">OUR PROGRAMS</h2>

    <div class="program-col col-one">
      <h2>HIIT</h2>
      <p>High intensity interval training is 30-45 minutes of fat burning fun. The class is a mix of cardio, bodyweight and some resistance movements.</p>
      <h2>CONDITIONING</h2>
      <p>A full hour of strength, cardio and bodyweight training to get you in tip top shape. Expect a mix of barbells, kettlebells, rowing machines, bikes and other training methods.</p>
      <h2>KPL</h2>
      <p>This is our big Friday session to set you up for the weekend. 90 minutes of hard training that is done with a team emphasis. From heavy lifting to cardio triathlons, this class has it all but not for the faint hearted.</p>
    </div>
    <div class="program-col col-two">
      <h2>MUAY THAI</h2>
      <p>Commonly known as the science of 8 limbs you will learn how to punch, kick, knee and elbow. Thailands national sport is a great way to get your fitness kick. We train the complete beginner all the way to international fighters so you are in great hands.</p>
      <h2>KIDS<br>MUAY THAI</h2>
      <p>Our junior program starts from age 6 onwards. Muay Thai is a great way for kids to get active and fit while learning new skills. Training in martial arts also teaches self discipline and socialisation skills.</p>
    </div>
    <div class="program-col col-three">
      <h2>YOGA</h2>
      <p>A combination of physical and mental practises that will leave you focused and refreshed for whatever the week throws at you. We always recommend our yoga classes as a great way to balance the high intensity training we offer.</p>
      <h2>U-PRESS</h2>
      <p>Strength training with a little bit of conditioning. We regularly update the program and re test lifts to ensure you are making progress and getting stronger.</p>
    </div>

    <div class="contact">
      <h3>CONTACT</h3>
      <div class="phone">07950362814</div>
      <div class="email">info@briskwatermotiongym.com</div>
    </div>
    <div class="footer-web">WWW.BRISKWATERMOTIONGYM.COM</div>
    <div class="address">Unit 42C, 273 Quillan Street, Fenwick Hollow, Glasgow, G72TR</div>
  </section>
</main>
</body>
</html>
```